Business Card Design

Locksmith, Safes, Security Systems, Camera Systems, Home Theater, Chip Keys & Remotes

Industry/Entity Type

Business

Contact Information for Business Card

Dorian Pelley Owner
2870 Fenwick Hollow Loop
Corley Springs, TN 37918
P 334-555-0148
F 334-555-0193
dpelley@tamblynkeys.com
www.tamblynkeys.com
AL Lic #5827
*Maybe follow us on Linkhall or Linkhall symbol

```html
<!DOCTYPE html>
<html lang="en">
<head>
<meta charset="utf-8">
<title>Tamblyn's Lock &amp; Security — Business Card</title>
<link href="https://fonts.googleapis.com/css2?family=Open+Sans:ital,wght@0,400;0,600;1,400;1,600&display=swap" rel="stylesheet">
<style>
  :root {
    --brand-blue: #2b3990;
    --accent-blue: #3a4ba8;
    --paper: #ffffff;
    --ink-grey: #4a4a4a;
    --backdrop: #e7e7ea;
  }
  * { margin: 0; padding: 0; box-sizing: border-box; }
  html, body { width: 1200px; height: 1200px; overflow: hidden; }
  body {
    background: var(--backdrop);
    font-family: "Open Sans", Arial, sans-serif;
    position: relative;
  }
  .card {
    position: absolute;
    left: 110px;
    width: 980px;
    height: 560px;
    border-radius: 6px;
    box-shadow: 0 6px 18px rgba(0,0,0,0.15);
    overflow: hidden;
  }
  .wordmark {
    font-family: "Open Sans", Arial, sans-serif;
    font-weight: 600;
    line-height: 1.1;
    white-space: nowrap;
  }

  /* Front side */
  .card-front { top: 30px; background: var(--brand-blue); color: var(--paper); }
  .front-info { position: absolute; left: 64px; top: 64px; }
  .card-front .wordmark { font-size: 46px; color: var(--paper); }
  .holder-name { font-weight: 600; font-size: 32px; margin-top: 40px; }
  .holder-role { font-size: 20px; margin-top: 4px; }
  .address { font-size: 20px; line-height: 1.45; margin-top: 14px; }
  .contact-list { list-style: none; margin-top: 8px; font-size: 20px; line-height: 1.6; }
  .contact-list li { display: flex; align-items: center; gap: 10px; }
  .contact-list svg { width: 20px; height: 20px; fill: var(--paper); }

  /* Back side */
  .card-back { top: 610px; background: var(--paper); color: var(--brand-blue); }
  .back-brand {
    position: absolute; left: 0; right: 0; top: 120px;
    display: flex; justify-content: center; align-items: center; gap: 20px;
  }
  .brand-mark-square { width: 56px; height: 56px; background: var(--brand-blue); }
  .card-back .wordmark { font-size: 44px; color: var(--brand-blue); }
  .services {
    position: absolute; left: 0; right: 0; top: 290px;
    text-align: center; color: var(--ink-grey);
    font-style: italic; font-weight: 600; font-size: 25px; line-height: 1.45;
  }
  .web-line {
    display: flex; justify-content: center; align-items: center; gap: 18px;
    margin-top: 6px; font-weight: 400; letter-spacing: 3px;
  }
  .rule { width: 70px; height: 3px; background: var(--accent-blue); border-radius: 2px; }
  .social {
    position: absolute; right: 40px; bottom: 36px;
    display: flex; align-items: center; gap: 10px;
    font-size: 18px; font-weight: 600; color: var(--accent-blue);
  }
  .social-square { width: 34px; height: 34px; border-radius: 6px; background: var(--accent-blue); }
</style>
</head>
<body>
  <section class="card card-front">
    <div class="front-info">
      <div class="wordmark">Tamblyn's Lock &amp; Security</div>
      <div class="holder-name">Dorian Pelley</div>
      <div class="holder-role">Owner</div>
      <div class="address">2870 Fenwick Hollow Loop Corley Springs<br>TN 37918<br>AL Lic #5827</div>
      <ul class="contact-list">
        <li>
          <svg viewBox="0 0 24 24" aria-hidden="true"><path d="M6.6 10.8a15.1 15.1 0 0 0 6.6 6.6l2.2-2.2a1 1 0 0 1 1-.25 11.4 11.4 0 0 0 3.6.57 1 1 0 0 1 1 1V20a1 1 0 0 1-1 1A17 17 0 0 1 3 4a1 1 0 0 1 1-1h3.5a1 1 0 0 1 1 1c0 1.25.2 2.45.57 3.6a1 1 0 0 1-.25 1z"/></svg>
          334-555-0148
        </li>
        <li>
          <svg viewBox="0 0 24 24" aria-hidden="true"><path d="M6 3h9l3 3v4H6z M4 11h16a2 2 0 0 1 2 2v7H2v-7a2 2 0 0 1 2-2z"/></svg>
          334-555-0193
        </li>
        <li>
          <svg viewBox="0 0 24 24" aria-hidden="true"><path d="M2 5h20v14H2z M3 6l9 7 9-7" stroke="#2b3990" stroke-width="1.6"/></svg>
          dpelley@tamblynkeys.com
        </li>
      </ul>
    </div>
  </section>

  <section class="card card-back">
    <div class="back-brand">
      <div class="brand-mark-square"></div>
      <div class="wordmark">Tamblyn's Lock &amp; Security</div>
    </div>
    <div class="services">
      <div>Locksmith, Safes, Security Systems, Camera Systems</div>
      <div>Home Theater, Chip Keys &amp; Remotes</div>
      <div class="web-line"><span class="rule"></span>www.tamblynkeys.com<span class="rule"></span></div>
    </div>
    <div class="social"><span class="social-square"></span>Linkhall</div>
  </section>
</body>
</html>
```